Poster Design Project

We are launching a new company Q Vizo, we sell advertising on digital signage and we are launching our company selling ads at our 2 locations, Barlow Heights Sports and Rec Club and the Merrowby Bay Sports and Rec Club. We want to advertise that we have 5 10 and 15 ad slots available and ads start from as little as $27.00 per week. We need to let people know we offer 10% discount to KNBTA members. it needs to have the following contact details to get more information, Marcus 0427359012 and marcus@qvizo.com.au. As a new launch we are offering for the first 10 customers one of 2 discounts, get 4 weeks free all you have to pay is the content creation fee ($99 for 5 second ad) or 4 weeks free and free content creation if you sign up to a 18 week contract.

Update: need the add to start wit something like this but you can be creative:

Need to get you message or brand out, Have you heard of digital sinage?
We have ads avaliable starting from $27 per week at one of our locations.

Or something like that, as i am introducing my company they dont know what i do you untill they read this poster.

Target Market(s)

Targeting small to medium buisness

Industry/Entity Type

Advertising

Requirements
Must have
• Logo

```html
<!DOCTYPE html>
<html lang="en">
<head>
<meta charset="utf-8">
<title>Q Vizo – Digital Signage Poster</title>
<link rel="stylesheet" href="https://fonts.googleapis.com/css2?family=Rammetto+One&family=Barlow+Semi+Condensed:wght@500&family=Open+Sans:wght@400;600;700&display=swap">
<style>
  :root {
    --backdrop: #e9eef3;
    --orange: #ef8a1a;
    --orange-soft: #f6b46a;
    --cream: #fdf4a8;
    --headline-shadow: #4a2a08;
    --bubble: #1e78a8;
    --bubble-dark: #0f5a80;
    --ink-blue: #1b4f9c;
    --paper: #ffffff;
  }
  * { box-sizing: border-box; margin: 0; padding: 0; }
  html, body { width: 1200px; height: 900px; overflow: hidden; }
  body { background: var(--backdrop); position: relative; font-family: "Open Sans", sans-serif; }

  .poster {
    position: absolute; left: 292px; top: 12px; width: 616px; height: 878px;
    overflow: hidden;
    background: linear-gradient(180deg, var(--orange) 0%, #f19a36 35%, var(--orange-soft) 55%, #fde6cc 70%, var(--paper) 82%);
    box-shadow: 0 4px 14px rgba(0,0,0,.35);
  }
  .lead-in {
    position: absolute; color: var(--paper); font-family: "Rammetto One", serif;
    font-size: 16px; text-shadow: 1px 2px 2px rgba(74,42,8,.6); text-align: center;
  }
  .hook {
    position: absolute; color: var(--cream); font-family: "Rammetto One", serif;
    line-height: 1.05; text-align: center; font-weight: 400;
    text-shadow: 2px 3px 3px var(--headline-shadow);
  }
  .hook--message { left: 28px; top: 58px; width: 290px; font-size: 30px; transform: rotate(-4deg); }
  .hook--signage { left: 350px; top: 58px; width: 220px; font-size: 33px; transform: rotate(2deg); }
  .lead-in--left { left: 30px; top: 32px; width: 270px; }
  .lead-in--right { left: 360px; top: 33px; width: 210px; }
  .lead-in--price { left: 0; width: 616px; top: 146px; font-size: 17px; }
  .price {
    position: absolute; left: 0; top: 176px; width: 616px; text-align: center;
    color: var(--cream); font-family: "Rammetto One", serif; font-size: 74px; line-height: 1;
    white-space: nowrap; transform: rotate(-2deg);
    text-shadow: 3px 3px 0 #2c3e50, 4px 5px 6px rgba(0,0,0,.4);
  }
  .glow {
    position: absolute; left: 40px; top: 230px; width: 560px; height: 300px;
    background: radial-gradient(ellipse at center, rgba(255,255,255,.5), rgba(255,255,255,0) 65%);
  }

  .bubbles { position: absolute; left: 0; top: 0; width: 616px; height: 878px; }
  .bubble-text {
    font-family: "Barlow Semi Condensed", sans-serif; font-weight: 500; fill: var(--paper);
    font-size: 17px;
  }

  .promo-photo {
    position: absolute; left: 0; top: 455px; width: 350px; height: 423px;
    background: linear-gradient(160deg, #f4f4f4 0%, #d9dde2 40%, #4a86c5 70%, #c79a7c 100%);
    clip-path: polygon(0 30%, 40% 0, 62% 2%, 78% 28%, 68% 60%, 72% 100%, 0 100%);
  }

  .offer { position: absolute; left: 296px; top: 605px; width: 300px; color: var(--ink-blue); }
  .offer__title { font-weight: 600; font-size: 16px; line-height: 1.35; }
  .offer__list { list-style: none; margin-top: 20px; }
  .offer__item { position: relative; padding-left: 20px; font-size: 12px; line-height: 1.3; margin-bottom: 14px; }
  .offer__item::before {
    content: ""; position: absolute; left: 1px; top: 5px; width: 7px; height: 7px; border-radius: 50%;
    background: var(--ink-blue);
  }

  .brand { position: absolute; left: 300px; top: 790px; display: flex; align-items: center; gap: 10px; }
  .brand__mark { width: 44px; height: 44px; background: var(--ink-blue); }
  .brand__name { font-family: "Open Sans", sans-serif; font-weight: 700; font-size: 34px; color: #111; }

  .contact { position: absolute; left: 483px; top: 795px; color: var(--ink-blue); font-size: 11.5px; font-weight: 600; line-height: 1.45; font-style: normal; }
</style>
</head>
<body>
  <main class="poster">
    <p class="lead-in lead-in--left">Do you need to get your</p>
    <h1 class="hook hook--message">mesage or brand out?</h1>
    <p class="lead-in lead-in--right">Have you heard of</p>
    <h2 class="hook hook--signage">Digital Signage?</h2>

    <p class="lead-in lead-in--price">Ads starting from</p>
    <div class="glow"></div>

    <svg class="bubbles" viewBox="0 0 616 878">
      <g fill="var(--bubble)" stroke="var(--bubble-dark)" stroke-width="2">
        <path d="M238 530 Q200 430 160 360 L195 352 Q222 440 246 528 Z"/>
        <path d="M240 528 Q300 430 335 365 L365 375 Q305 450 250 532 Z"/>
        <path d="M246 534 Q360 475 440 450 L450 478 Q360 505 250 540 Z"/>
        <ellipse cx="165" cy="318" rx="70" ry="56" transform="rotate(-25 165 318)"/>
        <ellipse cx="375" cy="305" rx="120" ry="72" transform="rotate(18 375 305)"/>
        <ellipse cx="510" cy="440" rx="78" ry="68" transform="rotate(20 510 440)"/>
      </g>
      <text class="bubble-text" transform="translate(165 318) rotate(-35)" text-anchor="middle">
        <tspan x="0" y="-12">5, 10 and</tspan><tspan x="0" dy="18">15 ad slots</tspan><tspan x="0" dy="18">available</tspan>
      </text>
      <text class="bubble-text" transform="translate(375 305) rotate(22)" text-anchor="middle">
        <tspan x="0" y="-21">located at Barlow</tspan><tspan x="0" dy="18">Heights Sports &amp; Rec</tspan><tspan x="0" dy="18">Club and Merrowby</tspan><tspan x="0" dy="18">Bay Sports &amp; Rec Club</tspan>
      </text>
      <text class="bubble-text" transform="translate(510 440) rotate(55)" text-anchor="middle">
        <tspan x="0" y="-3">10% discount to</tspan><tspan x="0" dy="18">KNBTA members</tspan>
      </text>
    </svg>

    <p class="price">$27 / week!</p>

    <div class="promo-photo" role="img" aria-label="Photo of a shouting man in blue glasses and bow tie holding a white and blue megaphone"></div>

    <section class="offer">
      <p class="offer__title">For the first 10 customers,<br>get any of the following discounts:</p>
      <ul class="offer__list">
        <li class="offer__item">get 4 weeks free and just pay<br>for the content creation fee<br>($99 for a 5 second ad)</li>
        <li class="offer__item">get 4 weeks free and free content creation<br>if you sign up for an 18 week contract</li>
      </ul>
    </section>

    <div class="brand">
      <span class="brand__mark"></span>
      <span class="brand__name">Q Vizo</span>
    </div>

    <address class="contact">
      Contact:<br>
      Marcus 0427359012<br>
      marcus@qvizo.com.au
    </address>
  </main>
</body>
</html>
```